Harbinger Crude Advisors needs a logo design and business card layout.

HCA is a consulting firm in oil and gas, specializing in upstream engineering and field work. We provide engineering solutions for the complete wellbore cycle from casing design to flowback. This includes completion and production design. On-site job supervision and project engineering for conventional and unconventional reservoirs. Asset analysis by reviewing operational conditions of asset packages to determine value of potential acquisitions or divesture.

```html
<!DOCTYPE html>
<html lang="en">
<head>
<meta charset="utf-8">
<title>Harbinger Crude Advisors – Business Card</title>
<link rel="stylesheet" href="https://fonts.googleapis.com/css2?family=Montserrat:wght@700&family=Arimo:ital,wght@0,400;0,700;1,700&display=swap">
<style>
  :root {
    --bg: #2b2b2d;
    --card-black: #0b0b0c;
    --card-white: #ffffff;
    --brand-blue: #1e88d2;
    --brand-blue-deep: #0b6fb8;
    --text-light: #ffffff;
  }
  * { margin: 0; padding: 0; box-sizing: border-box; }
  html, body { width: 1200px; height: 880px; overflow: hidden; }
  body {
    background: var(--bg);
    position: relative;
    font-family: "Arimo", Arial, sans-serif;
  }
  .card {
    position: absolute;
    border-radius: 16px;
    overflow: hidden;
  }

  /* Front side */
  .card-front {
    left: 110px; top: 290px;
    width: 540px; height: 310px;
    background: var(--card-black);
    display: flex; flex-direction: column;
    align-items: center; justify-content: center;
  }
  .brand { display: flex; align-items: center; gap: 14px; }
  .brand-dot {
    flex: none;
    width: 58px; height: 58px;
    border-radius: 50%;
    border: 6px solid var(--brand-blue);
  }
  .brand-name {
    font-family: "Montserrat", Arial, sans-serif;
    font-weight: 700;
    color: var(--brand-blue);
    font-size: 25px;
    line-height: 1.1;
    max-width: 270px;
  }
  .front-web {
    margin-top: 34px;
    font-size: 15px;
    letter-spacing: 3px;
    color: var(--brand-blue);
  }
  .front-web .prefix { color: var(--text-light); }

  /* Back side */
  .card-back {
    left: 760px; top: 180px;
    width: 310px; height: 530px;
    background: var(--card-white);
  }
  .back-brand {
    position: absolute; top: 40px; left: 0; right: 0;
    display: flex; flex-direction: column; align-items: center; gap: 12px;
  }
  .back-brand .brand-dot { width: 64px; height: 64px; }
  .back-brand .brand-name { text-align: center; font-size: 22px; max-width: 240px; }
  .swoosh { position: absolute; left: 0; top: 0; }
  .contact {
    position: absolute; right: 26px; top: 298px; width: 250px;
    text-align: right; color: var(--text-light);
  }
  .contact-name { font-size: 21px; line-height: 24px; font-weight: 700; }
  .contact-role { font-size: 15px; line-height: 18px; color: var(--brand-blue); margin-top: 2px; }
  .contact-row {
    border-top: 1px solid var(--brand-blue-deep);
    margin-top: 9px; padding-top: 6px;
    font-size: 14px; line-height: 16px;
  }
  .contact-label {
    display: block; color: var(--brand-blue);
    font-weight: 700; font-style: italic; font-size: 13px; line-height: 15px;
  }
  .back-band {
    position: absolute; left: 0; right: 0; bottom: 0; height: 44px;
    background: linear-gradient(90deg, var(--brand-blue), var(--brand-blue-deep));
    border-top: 5px solid var(--card-white);
    display: flex; align-items: center; justify-content: center;
    color: var(--card-black); font-size: 15px;
  }
</style>
</head>
<body>

  <section class="card card-front" aria-label="Card front">
    <div class="brand">
      <span class="brand-dot"></span>
      <span class="brand-name">Harbinger Crude Advisors</span>
    </div>
    <p class="front-web"><span class="prefix">www.</span>harbingercrude.com</p>
  </section>

  <section class="card card-back" aria-label="Card back">
    <div class="back-brand">
      <span class="brand-dot"></span>
      <span class="brand-name">Harbinger Crude Advisors</span>
    </div>
    <svg class="swoosh" width="310" height="530" viewBox="0 0 310 530" aria-hidden="true">
      <path d="M0 186 C 120 184, 250 206, 310 262 L310 530 L0 530 Z" fill="var(--brand-blue)"/>
      <path d="M0 194 C 120 194, 242 214, 310 272 L310 530 L0 530 Z" fill="var(--card-white)"/>
      <path d="M0 200 C 120 200, 238 220, 310 282 L310 530 L0 530 Z" fill="var(--card-black)"/>
      <path d="M40 212 C 140 214, 226 236, 286 278" stroke="var(--card-white)" stroke-width="1.5" fill="none"/>
    </svg>
    <div class="contact">
      <p class="contact-name">Dara Whitlow</p>
      <p class="contact-role">Marketing Officer</p>
      <p class="contact-row"><span class="contact-label">Cell:</span>(214) 555 0187</p>
      <p class="contact-row"><span class="contact-label">Email:</span>hello@harbingercrude.com</p>
      <p class="contact-row">PO BOX 48, Mill Road<br>Eastgate, Leeds</p>
    </div>
    <div class="back-band">www.harbingercrude.com</div>
  </section>

</body>
</html>
```